Brochure for Custom Cabinets Manufacturing Company

We need a design for the brochure for company that is doing high end cabinets for homes. The following information may be included:

Custom made Kitchens and Cabinets Company, located in Calgary.

Why us:

Availability. All kitchens are manufactured in a wide range of prices. Searching for a suitable option is easy and fun.

High quality. Our company tends to European standards. This involves the careful selection of raw materials, hardware, as well as a neat assembly.
High quality of our product is achieved through the use of modern equipment and advanced technology.

Wide selection. Selling our product includes hundreds of different options: in styles, materials, designs, and colors. All products are easy to use, functional and custom made design.

Happy Clients. We are taking into account all the wishes of our customers. We also provide warranty and customer service to bring positive emotions to our clients.

Proudly Canadian made. Calgary based production of our products. Custom orders without delays.

Superior health and safety standards.

```html
<!DOCTYPE html>
<html lang="en">
<head>
<meta charset="utf-8">
<title>Cedarline Interiors – Brochure</title>
<link rel="stylesheet" href="https://fonts.googleapis.com/css2?family=Roboto:wght@300;400;500;700&family=Didact+Gothic&display=swap">
<style>
  :root {
    --backdrop: #5b5b5b;
    --paper: #f4f4f4;
    --green: #63b33a;
    --blue: #1f6fc6;
    --ink: #222;
    --ink-soft: #3a3a3a;
    --tagline: #2c3a92;
    --white: #fff;
  }
  * { box-sizing: border-box; margin: 0; padding: 0; }
  html, body { width: 1200px; height: 830px; overflow: hidden; }
  body { background: var(--backdrop); position: relative; font-family: "Didact Gothic", "Century Gothic", sans-serif; }

  .page { position: absolute; top: 26px; width: 550px; height: 778px; background: var(--paper); overflow: hidden; }
  .page--back { left: 29px; }
  .page--front { left: 615px; }
  .layer { position: absolute; left: 0; top: 0; width: 550px; height: 778px; }

  .photo { position: absolute; left: 0; width: 550px; }
  .photo--kitchen-open { top: 0; height: 250px;
    background: linear-gradient(100deg, #dfe3e6 0%, #c9c6c0 30%, #7a5a45 48%, #d9d6d0 62%, #f2f2f0 80%, #e6e4e0 100%); }
  .photo--kitchen-island { top: 80px; height: 600px;
    background: linear-gradient(180deg, #e8e2d6 0%, #ddd3c2 35%, #c9b9a2 48%, #8c3f22 62%, #7a3018 80%, #5a2a1c 100%); }

  .why-title { position: absolute; left: 40px; top: 211px; font: 700 18px "Roboto", sans-serif; color: var(--ink); }
  .reason { position: absolute; left: 56px; width: 445px; }
  .reason__icon { position: absolute; left: 0; top: 0; width: 36px; height: 36px; border-radius: 8px; }
  .reason__icon--search { background: linear-gradient(135deg, #7dc043, #2c5a1e); border-radius: 50%; }
  .reason__icon--quality { background: linear-gradient(135deg, #6fb6f0, #1f6fc6); }
  .reason__icon--selection { background: linear-gradient(135deg, #555, #1a1a1a); }
  .reason__icon--clients { background: linear-gradient(135deg, #3e8fe0, #1b3f8c); }
  .reason__title { position: absolute; left: 53px; top: 0; font: 500 13px "Roboto", sans-serif; color: var(--ink); }
  .reason__text { position: absolute; left: 53px; top: 22px; width: 392px; font-size: 9.4px; line-height: 11.4px; color: var(--ink-soft); text-align: justify; }
  .reason__text + .reason__text { top: 56px; }

  .tagline { position: absolute; left: 47px; top: 562px; font: 300 21px/28px "Roboto", sans-serif; color: var(--tagline); }

  .headline { position: absolute; left: 29px; top: 40px; font: 300 21px "Roboto", sans-serif; color: var(--tagline); }
  .masthead-mark { position: absolute; left: 400px; top: 30px; width: 80px; height: 80px; border: 5px solid var(--green); border-radius: 6px; background: var(--white); }
  .masthead-name { position: absolute; right: 28px; top: 120px; font: 500 27px "Roboto", sans-serif; color: var(--blue); }

  .banner { position: absolute; left: 41px; top: 498px; width: 470px; height: 74px; background: var(--blue); display: flex; align-items: center; justify-content: center; text-align: center; font: 300 22px/33px "Roboto", sans-serif; color: var(--white); text-transform: uppercase; }

  .brand { position: absolute; left: 357px; top: 664px; display: flex; align-items: center; gap: 9px; }
  .brand__square { width: 42px; height: 42px; border: 3px solid var(--white); border-radius: 3px; }
  .brand__name { font: 500 21px "Roboto", sans-serif; color: var(--white); }

  .contact { position: absolute; color: var(--white); display: flex; flex-direction: column; }
  .contact__row { display: flex; align-items: center; gap: 4px; white-space: nowrap; }
  .contact--address { left: 24px; top: 724px; font-size: 8.8px; line-height: 12.5px; }
  .contact--address .fax { margin-top: 6px; }
  .contact--main { left: 191px; top: 712px; font-size: 9px; line-height: 15px; }
  .contact--main .big { font: 300 17px/22px "Roboto", sans-serif; }
  .contact--local { left: 401px; top: 718px; font: 300 18px/27px "Roboto", sans-serif; }
  .contact svg { flex: none; fill: var(--white); }
  .indent { padding-left: 10px; }
</style>
</head>
<body>

<section class="page page--back">
  <div class="photo photo--kitchen-open" role="img" aria-label="Photo of a modern open kitchen with walnut and white cabinets, island and pendant lights"></div>
  <svg class="layer" viewBox="0 0 550 778" aria-hidden="true">
    <defs>
      <linearGradient id="footBlueA" x1="0" y1="0" x2="0" y2="1"><stop offset="0" stop-color="#2a86d8"/><stop offset="1" stop-color="#1646a8"/></linearGradient>
    </defs>
    <path d="M0,200 C120,205 260,250 400,252 C470,253 520,240 550,222 L550,778 L0,778 Z" fill="var(--paper)"/>
    <path d="M0,146 C150,140 270,228 420,238 C480,241 530,225 550,205 L550,222 C520,240 470,253 400,252 C260,250 120,205 0,200 Z" fill="var(--green)"/>
    <path d="M0,650 C180,655 360,590 550,598 L550,640 C370,640 180,700 0,700 Z" fill="var(--green)"/>
    <path d="M0,708 C180,708 370,650 550,650 L550,778 L0,778 Z" fill="url(#footBlueA)"/>
  </svg>

  <h2 class="why-title">Why Choose Us?</h2>

  <div class="reason" style="top:258px">
    <div class="reason__icon reason__icon--search" role="img" aria-label="Magnifying glass icon"></div>
    <h3 class="reason__title">Availability.</h3>
    <p class="reason__text">All kitchens are manufactured in a wide range of prices. Searching for a suitable option is easy and fun.</p>
  </div>
  <div class="reason" style="top:328px">
    <div class="reason__icon reason__icon--quality" role="img" aria-label="Thumbs-up icon"></div>
    <h3 class="reason__title">High quality.</h3>
    <p class="reason__text">Our company trends to high quality standards. This involves the careful selection of raw materials, hardware, as well as a neat assembly.</p>
    <p class="reason__text">High quality of our product is achieved through the use of modern equipment and advanced technology.</p>
  </div>
  <div class="reason" style="top:430px">
    <div class="reason__icon reason__icon--selection" role="img" aria-label="Catalogue with colour swatch icon"></div>
    <h3 class="reason__title">Wide selection.</h3>
    <p class="reason__text">Selling our product includes hundreds of different options: in styles, materials, designs, and colors. All products are easy to use, functional and custom made design.</p>
  </div>
  <div class="reason" style="top:500px">
    <div class="reason__icon reason__icon--clients" role="img" aria-label="Happy tablet character icon"></div>
    <h3 class="reason__title">Happy Clients.</h3>
    <p class="reason__text">We are taking into account all the wishes of our customers. We also provide warranty and customer service to bring positive emotions to our clients.</p>
  </div>

  <p class="tagline">Proudly Canadian made. Calgary based production.<br>Custom orders without delays.</p>

  <div class="brand"><span class="brand__square"></span><span class="brand__name">Cedarline</span></div>

  <div class="contact contact--address">
    <span class="contact__row"><svg width="7" height="9" viewBox="0 0 10 14"><path d="M5 0a5 5 0 0 1 5 5c0 4-5 9-5 9S0 9 0 5a5 5 0 0 1 5-5zm0 3a2 2 0 1 0 0 4 2 2 0 0 0 0-4z"/></svg>1420 BIRCHMOUNT ROAD NE, CALGARY,</span>
    <span class="indent">ALBERTA, CANADA, T2B 3K9</span>
    <span class="contact__row fax"><svg width="10" height="8" viewBox="0 0 10 8"><rect x="0" y="3" width="10" height="5" rx="1"/><rect x="2" y="0" width="6" height="3"/></svg>403.555.0129</span>
  </div>
  <div class="contact contact--main">
    <span class="contact__row big"><svg width="14" height="14" viewBox="0 0 14 14"><circle cx="7" cy="7" r="6.3" fill="none" stroke="#fff" stroke-width="1.2"/><path d="M4.5 3.5l1.5 0 .6 2-1 .8c.5 1.2 1.3 2 2.4 2.5l.8-1 2 .6v1.5c-3.5.2-6.5-2.8-6.3-6.4z"/></svg>1.800.555.0142</span>
    <span class="contact__row"><svg width="11" height="8" viewBox="0 0 11 8"><rect x=".5" y=".5" width="10" height="7" fill="none" stroke="#fff"/><path d="M.5.5l5 4 5-4" fill="none" stroke="#fff"/></svg>info@CedarlineInteriors.ca</span>
    <span class="contact__row"><svg width="10" height="10" viewBox="0 0 10 10"><circle cx="5" cy="5" r="4.4" fill="none" stroke="#fff"/><path d="M.6 5h8.8M5 .6c-2.4 2.6-2.4 6.2 0 8.8M5 .6c2.4 2.6 2.4 6.2 0 8.8" fill="none" stroke="#fff" stroke-width=".8"/></svg>www.CedarlineInteriors.ca</span>
  </div>
  <div class="contact contact--local">
    <span class="contact__row"><svg width="15" height="15" viewBox="0 0 14 14"><circle cx="7" cy="7" r="6.3" fill="none" stroke="#fff" stroke-width="1.2"/><path d="M4.5 3.5l1.5 0 .6 2-1 .8c.5 1.2 1.3 2 2.4 2.5l.8-1 2 .6v1.5c-3.5.2-6.5-2.8-6.3-6.4z"/></svg>403.555.0187</span>
    <span class="contact__row"><svg width="11" height="16" viewBox="0 0 11 16"><rect x=".7" y=".7" width="9.6" height="14.6" rx="1.5" fill="none" stroke="#fff" stroke-width="1.4"/><rect x="2.5" y="2.5" width="6" height="8"/></svg>403.555.0163</span>
  </div>
</section>

<section class="page page--front">
  <div class="photo photo--kitchen-island" role="img" aria-label="Photo of a kitchen with cream upper cabinets, steel range hood and a cherry wood island with cooktop"></div>
  <svg class="layer" viewBox="0 0 550 778" aria-hidden="true">
    <defs>
      <linearGradient id="footBlueB" x1="0" y1="0" x2="0" y2="1"><stop offset="0" stop-color="#2a86d8"/><stop offset="1" stop-color="#1646a8"/></linearGradient>
    </defs>
    <path d="M0,0 H550 V160 C420,175 300,140 200,110 C120,88 50,85 0,92 Z" fill="var(--paper)"/>
    <path d="M0,92 C50,85 120,88 200,110 C300,140 420,175 550,160 L550,190 C420,215 250,200 150,185 C90,178 40,180 0,186 Z" fill="var(--green)"/>
    <path d="M0,650 C180,655 360,590 550,598 L550,778 L0,778 Z" fill="var(--paper)"/>
    <path d="M0,650 C180,655 360,590 550,598 L550,640 C370,640 180,700 0,700 Z" fill="var(--green)"/>
    <path d="M0,708 C180,708 370,650 550,650 L550,778 L0,778 Z" fill="url(#footBlueB)"/>
  </svg>

  <h1 class="headline">Fulfilling Your Dreams in Colors</h1>
  <span class="masthead-mark"></span>
  <span class="masthead-name">Cedarline</span>

  <p class="banner">Custom made kitchens and cabinets<br>company, located in Calgary</p>

  <div class="brand"><span class="brand__square"></span><span class="brand__name">Cedarline</span></div>

  <div class="contact contact--address">
    <span class="contact__row"><svg width="7" height="9" viewBox="0 0 10 14"><path d="M5 0a5 5 0 0 1 5 5c0 4-5 9-5 9S0 9 0 5a5 5 0 0 1 5-5zm0 3a2 2 0 1 0 0 4 2 2 0 0 0 0-4z"/></svg>1420 BIRCHMOUNT ROAD NE, CALGARY,</span>
    <span class="indent">ALBERTA, CANADA, T2B 3K9</span>
    <span class="contact__row fax"><svg width="10" height="8" viewBox="0 0 10 8"><rect x="0" y="3" width="10" height="5" rx="1"/><rect x="2" y="0" width="6" height="3"/></svg>403.555.0129</span>
  </div>
  <div class="contact contact--main">
    <span class="contact__row big"><svg width="14" height="14" viewBox="0 0 14 14"><circle cx="7" cy="7" r="6.3" fill="none" stroke="#fff" stroke-width="1.2"/><path d="M4.5 3.5l1.5 0 .6 2-1 .8c.5 1.2 1.3 2 2.4 2.5l.8-1 2 .6v1.5c-3.5.2-6.5-2.8-6.3-6.4z"/></svg>1.800.555.0142</span>
    <span class="contact__row"><svg width="11" height="8" viewBox="0 0 11 8"><rect x=".5" y=".5" width="10" height="7" fill="none" stroke="#fff"/><path d="M.5.5l5 4 5-4" fill="none" stroke="#fff"/></svg>info@CedarlineInteriors.ca</span>
    <span class="contact__row"><svg width="10" height="10" viewBox="0 0 10 10"><circle cx="5" cy="5" r="4.4" fill="none" stroke="#fff"/><path d="M.6 5h8.8M5 .6c-2.4 2.6-2.4 6.2 0 8.8M5 .6c2.4 2.6 2.4 6.2 0 8.8" fill="none" stroke="#fff" stroke-width=".8"/></svg>www.CedarlineInteriors.ca</span>
  </div>
  <div class="contact contact--local">
    <span class="contact__row"><svg width="15" height="15" viewBox="0 0 14 14"><circle cx="7" cy="7" r="6.3" fill="none" stroke="#fff" stroke-width="1.2"/><path d="M4.5 3.5l1.5 0 .6 2-1 .8c.5 1.2 1.3 2 2.4 2.5l.8-1 2 .6v1.5c-3.5.2-6.5-2.8-6.3-6.4z"/></svg>403.555.0187</span>
    <span class="contact__row"><svg width="11" height="16" viewBox="0 0 11 16"><rect x=".7" y=".7" width="9.6" height="14.6" rx="1.5" fill="none" stroke="#fff" stroke-width="1.4"/><rect x="2.5" y="2.5" width="6" height="8"/></svg>403.555.0163</span>
  </div>
</section>

</body>
</html>
```